Letterhead Design Project

Quillfern Consulting is a newly created boutique consultancy focussing on delivering strategic consulting to medium and large businesses, with a focus on:
- Strategic planning and execution.
- Corporate function optimisation, especially in the areas of finance, commercial, and IT. This includes implementing the right functional design for the needs of the business, and ensuring the right skills.
- Performance management, in particular project governance and control, operational metrics and management reporting.
I have in mind a tag line for the business being:
"Guiding firms toward lasting, measurable growth."
I am looking for a letterhead design which utilises my new logo on report templates (powerpoint and word), and letterhead.
Lexiborn defines a mother lode as follows:
"Mother lode is a principal vein or zone of veins of gold or silver ore. The term probably came from a literal translation of the Spanish veta madre, a term common in old Mexican mining. Veta madre, for instance, is the name given to an 11-kilometre-long (6.8 mi) silver vein discovered in 1548 in Guanajuato, New Spain (modern-day Mexico)."
My preference is for black and gold. Logo files are attached in .eps format. All fonts are outlined. The fonts that are used are "Crimson Text" and "Josefin Sans". They are free open source fonts and they are available here: http://www.glyphbarn.com/fonts
Target Market(s)
Medium to large corporates.
Industry/Entity Type
Boutique
Other font styles liked:
- All fonts are outlined. The fonts that are used are "Crimson Text" and "Josefin Sans". They are free open source fonts and they are available here: http://www.glyphbarn.com/fonts

```html
<!DOCTYPE html>
<html lang="en">
<head>
<meta charset="UTF-8">
<title>Quillfern Consulting — Letterhead</title>
<link rel="stylesheet" href="https://fonts.googleapis.com/css2?family=Crimson+Text:wght@400;600&family=Josefin+Sans:wght@400&display=swap">
<style>
  :root {
    --backdrop: #e6e2dc;
    --paper: #ffffff;
    --ink: #111111;
    --gold: #d9a520;
    --tagline: #333333;
  }
  * { margin: 0; padding: 0; box-sizing: border-box; }
  html, body {
    width: 1200px;
    height: 899px;
    overflow: hidden;
    background: var(--backdrop);
  }
  .letterhead {
    position: absolute;
    left: 305px;
    top: 50px;
    width: 613px;
    height: 793px;
    background: var(--paper);
  }
  .band-black {
    position: absolute;
    left: 0;
    top: 0;
    width: 42px;
    height: 100%;
    background: var(--ink);
  }
  .band-gold {
    position: absolute;
    left: 46px;
    top: 0;
    width: 11px;
    height: 100%;
    background: var(--gold);
  }
  .brand {
    position: absolute;
    left: 0;
    right: 0;
    top: 24px;
    display: flex;
    flex-direction: column;
    align-items: center;
    gap: 18px;
  }
  .brand-square {
    width: 62px;
    height: 62px;
    background: var(--gold);
  }
  .brand-name {
    font-family: "Crimson Text", Georgia, serif;
    font-weight: 400;
    font-size: 24px;
    letter-spacing: 1px;
    text-transform: uppercase;
    color: var(--ink);
    line-height: 1;
  }
  .tagline {
    position: absolute;
    left: 0;
    right: 0;
    bottom: 8px;
    text-align: center;
    font-family: "Crimson Text", Georgia, serif;
    font-size: 10px;
    letter-spacing: 1px;
    text-transform: uppercase;
    color: var(--tagline);
  }
</style>
</head>
<body>
  <main class="letterhead">
    <div class="band-black"></div>
    <div class="band-gold"></div>
    <header class="brand">
      <span class="brand-square"></span>
      <span class="brand-name">Quillfern Consulting</span>
    </header>
    <p class="tagline">"Guiding firms toward lasting, measurable growth."</p>
  </main>
</body>
</html>
```